Life Coaching Business - needs business card design with logo

I need a business card and logo design for a life coaching business I started based in Los Angeles. I offer services to clients that wish to bring more balance and overall wholeness to their lives. As of right now, the business name is "Marcus Ellery Coaching." An iidea I had for the logo was to be kind of a Yin-Yang symbol but with dolphins, as the dolphin has symbolic meaning for my business. Although I am really open to other ideas as long as it incorporates the idea of “balance,” “wholeness,” and “dolphins.”I also wanted to incorporate the color blue, maybe in the form of water, waves, or some sort of peaceful imagery.

```html
<!DOCTYPE html>
<html lang="en">
<head>
<meta charset="utf-8">
<title>Marcus Ellery Coaching – Business Card</title>
<link rel="stylesheet" href="https://fonts.googleapis.com/css2?family=Libre+Baskerville:wght@400;700&display=swap">
<style>
  :root {
    --stage: #e9ecf0;
    --blue-light: #46b0e6;
    --blue-mid: #2f86cf;
    --blue-deep: #1d5aa9;
    --ink-blue: #2458a6;
    --ink-grey: #4a4a4a;
    --rule-grey: #8c8c8c;
    --paper: #ffffff;
  }
  * { margin: 0; padding: 0; box-sizing: border-box; }
  html, body {
    width: 1200px; height: 800px; overflow: hidden;
    background: var(--stage);
    font-family: "Libre Baskerville", Georgia, serif;
  }
  .canvas { position: relative; width: 1200px; height: 800px; }

  .card {
    position: absolute;
    width: 540px; height: 309px;
    overflow: hidden;
    box-shadow: 0 14px 30px rgba(20, 40, 70, 0.22);
  }

  /* Back side */
  .card--back {
    left: 60px; top: 110px;
    background: linear-gradient(135deg, var(--blue-light) 0%, var(--blue-mid) 45%, var(--blue-deep) 100%);
    display: flex; flex-direction: column; align-items: center; justify-content: center;
    gap: 18px;
  }
  .back-mark {
    width: 74px; height: 74px; border-radius: 50%;
    background: var(--paper);
  }
  .back-name {
    color: var(--paper);
    font-weight: 700; font-size: 22px; letter-spacing: 0.5px;
    text-transform: uppercase;
  }

  /* Front side */
  .card--front {
    left: 600px; top: 380px;
    background: var(--paper);
  }
  .front-art { position: absolute; inset: 0; }
  .front-name {
    position: absolute; right: 36px; top: 42px;
    color: var(--ink-blue);
    font-weight: 700; font-size: 20px; letter-spacing: 0.4px;
    text-transform: uppercase;
    padding-bottom: 8px;
    border-bottom: 1px solid var(--rule-grey);
  }
  .contact {
    position: absolute; right: 28px; top: 118px;
    list-style: none;
    color: var(--ink-grey);
    font-size: 12.5px; line-height: 1.55;
    text-align: right;
  }
  .contact__item { display: flex; align-items: center; justify-content: flex-end; gap: 8px; }
  .contact__item--spaced { margin-top: 8px; }
  .contact__text { display: block; }
  .contact__icon { width: 16px; height: 16px; flex: none; }
  .contact__icon--blank { visibility: hidden; }
</style>
</head>
<body>
<main class="canvas">

  <section class="card card--back" aria-label="Card back">
    <div class="back-mark" aria-hidden="true"></div>
    <p class="back-name">Marcus Ellery Coaching</p>
  </section>

  <section class="card card--front" aria-label="Card front">
    <svg class="front-art" viewBox="0 0 540 309" aria-hidden="true">
      <defs>
        <linearGradient id="band-blue" x1="0" y1="0" x2="1" y2="1">
          <stop offset="0" stop-color="var(--blue-light)"/>
          <stop offset="1" stop-color="var(--blue-deep)"/>
        </linearGradient>
        <linearGradient id="disc-blue" x1="0" y1="0" x2="1" y2="1">
          <stop offset="0" stop-color="#2fa9e2"/>
          <stop offset="1" stop-color="#1f64b2"/>
        </linearGradient>
      </defs>
      <path d="M0 150 C 90 130, 200 170, 260 230 C 290 262, 305 290, 310 309 L 0 309 Z" fill="url(#band-blue)"/>
      <circle cx="195" cy="235" r="118" fill="url(#disc-blue)" stroke="var(--paper)" stroke-width="9"/>
    </svg>

    <p class="front-name">Marcus Ellery Coaching</p>

    <ul class="contact">
      <li class="contact__item">
        <span class="contact__text">1480 Harbor View Dr.</span>
        <svg class="contact__icon contact__icon--blank" viewBox="0 0 16 16" aria-hidden="true"></svg>
      </li>
      <li class="contact__item">
        <span class="contact__text">Suite 210, Los Angeles</span>
        <svg class="contact__icon" viewBox="0 0 16 16" aria-hidden="true">
          <circle cx="8" cy="8" r="8" fill="var(--ink-blue)"/>
          <path d="M8 3.5a3 3 0 0 0-3 3c0 2.3 3 5.8 3 5.8s3-3.5 3-5.8a3 3 0 0 0-3-3zm0 4.1a1.1 1.1 0 1 1 0-2.2 1.1 1.1 0 0 1 0 2.2z" fill="var(--paper)"/>
        </svg>
      </li>
      <li class="contact__item contact__item--spaced">
        <span class="contact__text">310-555-0142</span>
        <svg class="contact__icon" viewBox="0 0 16 16" aria-hidden="true">
          <circle cx="8" cy="8" r="8" fill="var(--ink-blue)"/>
          <path d="M5.3 4.2l1.4-.3.8 2-1 .8a5.5 5.5 0 0 0 2.8 2.8l.8-1 2 .8-.3 1.4c-.2.6-.8.9-1.4.8A7.2 7.2 0 0 1 4.5 5.6c-.1-.6.2-1.2.8-1.4z" fill="var(--paper)"/>
        </svg>
      </li>
      <li class="contact__item">
        <span class="contact__text">hello@marcusellery.com</span>
        <svg class="contact__icon" viewBox="0 0 16 16" aria-hidden="true">
          <circle cx="8" cy="8" r="8" fill="var(--ink-blue)"/>
          <rect x="4" y="5.2" width="8" height="5.6" rx="0.6" fill="var(--paper)"/>
          <path d="M4.3 5.6L8 8.4l3.7-2.8" fill="none" stroke="var(--ink-blue)" stroke-width="0.9"/>
        </svg>
      </li>
      <li class="contact__item">
        <span class="contact__text">www.marcusellery.com</span>
        <svg class="contact__icon" viewBox="0 0 16 16" aria-hidden="true">
          <circle cx="8" cy="8" r="8" fill="var(--ink-blue)"/>
          <g fill="none" stroke="var(--paper)" stroke-width="0.9">
            <circle cx="8" cy="8" r="4"/>
            <ellipse cx="8" cy="8" rx="1.8" ry="4"/>
            <path d="M4 8h8"/>
          </g>
        </svg>
      </li>
    </ul>
  </section>

</main>
</body>
</html>
```